Create Website for new company called "Verdant Lodge 17"

Verdant Lodge 17 is a new business situated in Southwestern Colorado. We are creating a business that will rent out spaces where clients can grow their own marijuana. Picture a large green house with partitioned spaces that are secured by a lock. Best way to envision this would be to think of a storage business that rents out storage rooms. The difference is that we will be having the units inside a green house ( for growing purposes) Picture a small area that is secured by locks, Picture an area that has the ability to provide state of the art security, cameras etc. We want to focus our efforts on professionals, blue collar workers and end users of marijuana. Our emphasis is in the area of assisting those whom wish to grow their own plants. We want to provide them a safe facility in which to do that. . Keep in mind that we also build custom grow rooms at clients homes and provide a grow pod (lease these) where a small grow unit will be delivered and picked up from our clients whom want to lease a unit for a short amount of time. We have a business card ( just designed) and will send that information to those whom express an interests in this project. We want to be able to sign people up for our services by entering an agreement and signing the agreement while on the internet. We want to provide our services to those whom consume recreational and medical marijuana. This site will need to gather information I.e email addresses so that we can followup with offers. This is a tremendous opportunity for the right designer. We will be creating many more websites as other states come on line and make marijuana legal to consume. Use the business card model for a point of reference of how we envision the concept. That is a business card we just recently printed. The hands and the plant is our logo so far. Open to suggestions. There will be three levels of service. Bronze, Silver, Gold or Platinum. We will also have a retail biz down the road but not at the present time.

Target Market(s)

Ages 21-60

Industry/Entity Type

Medical

Logo Text

Verdant Lodge 17.

Number of Pages Required

5+ page

Requirements
Must have
• Clean appearance not to busy , easily navigable from link to link, page to page. Must have ability down the road to enter into a contractual agreement via the website. Must use our provided logo and example of that is on our business card that will be uploaded here shortly. We would like to have the colors that are on the business card however if you have suggestions or color schemes that you want us to consider that is okay.
Nice to have
• Nice to have a animation of seed to weed and how clients can save a tremendous amount of money growing their own cannabis. Nice to have testimonial page or feedback page. Have a membership component to website,
Should not have
• No flashing lights, etc. Not to busy in terms of animations.

```html
<!DOCTYPE html>
<html lang="en">
<head>
<meta charset="utf-8">
<title>Verdant Lodge 17</title>
<link href="https://fonts.googleapis.com/css2?family=Oswald:wght@300;400&family=Arimo:wght@400;700&display=swap" rel="stylesheet">
<style>
:root{
  --leaf:#5f7d1a;
  --leaf-dark:#4a5f17;
  --slate:#2f3b3a;
  --forest:#0b7a3a;
  --mint:#2bd66a;
  --amber:#d97a2e;
  --amber-light:#f0a468;
  --ink:#333;
  --white:#fff;
}
*{box-sizing:border-box;margin:0;padding:0}
html,body{width:1116px;height:1200px;overflow:hidden}
body{position:relative;background:var(--leaf);font-family:"Arimo",Arial,sans-serif;color:var(--ink)}
a{text-decoration:none;color:inherit}
.abs{position:absolute}

/* header */
.brand-plate{left:72px;top:0;width:366px;height:168px}
.brand-name{left:72px;top:58px;width:366px;text-align:center;font-family:"Oswald",sans-serif;font-weight:400;font-size:40px;color:var(--slate);letter-spacing:1px}
.brand-dot{left:237px;top:14px;width:36px;height:36px;border-radius:50%;background:var(--forest)}
.account{right:82px;top:20px;font-family:"Oswald",sans-serif;font-weight:300;font-size:15px;color:var(--white)}
.account span{margin:0 5px}
.main-nav{left:523px;top:80px;display:flex;font-family:"Oswald",sans-serif;font-weight:300;font-size:19px;color:var(--white)}
.main-nav a{height:33px;line-height:33px;margin-right:27px}
.main-nav a.current{background:var(--slate);padding:0 21px;margin-right:12px}

/* hero */
.hero{left:0;top:187px;width:1116px;height:368px;background:linear-gradient(135deg,#6f9a3a,#3e6b22 45%,#8cb45a 75%,#4d7a2c)}
.slider-frame{left:72px;top:208px;width:662px;height:320px;background:var(--white)}
.slide-photo{left:82px;top:218px;width:643px;height:300px;background:linear-gradient(120deg,#2a2d2c 0%,#4f7a36 40%,#9fc27a 70%,#d7dcd1 100%)}
.slide-caption{left:82px;top:443px;width:643px;height:75px;background:rgba(30,32,32,.75);color:var(--white);font-family:"Oswald",sans-serif;font-weight:300;font-size:27px;line-height:75px;text-align:center}
.slide-arrow{top:336px;width:22px;height:50px}
.welcome-frame{left:754px;top:208px;width:290px;height:320px;background:var(--slate)}
.welcome-card{left:764px;top:218px;width:271px;height:300px;background:var(--white);padding:2px 10px 0;text-align:center;overflow:hidden}
.welcome-card h2{font-family:"Oswald",sans-serif;font-weight:300;font-size:26px;line-height:32px;color:var(--slate)}
.welcome-card h2 strong{display:block;font-weight:300;color:var(--forest)}
.welcome-card p{font-size:12.2px;line-height:16px;letter-spacing:.2px;text-align:left;margin-top:8px}
.welcome-card p + p{margin-top:14px}
.btn{display:inline-block;font-family:"Oswald",sans-serif;font-weight:300;color:var(--white);text-align:center}
.btn-more{position:absolute;left:77px;top:264px;width:116px;height:28px;line-height:24px;font-size:17px;background:var(--amber);border:2px solid var(--amber-light)}

/* services */
.service{top:575px;width:310px;height:298px;background:var(--white);border-radius:5px;overflow:hidden}
.service > svg{position:absolute;left:0;top:0}
.service h3{position:relative;font-family:"Oswald",sans-serif;font-weight:300;font-size:24px;line-height:36px;color:var(--white);text-align:center;padding-top:10px}
.service p{position:relative;font-size:12.2px;line-height:16.5px;letter-spacing:.3px;text-align:left;padding:0 18px;margin-top:30px}
.service p + p{margin-top:16px}
.btn-buy{position:absolute;left:112px;top:264px;width:88px;height:28px;line-height:24px;font-size:17px;border:2px solid}
.btn-buy svg{vertical-align:-3px;margin-right:8px}
.bronze .btn-buy{background:var(--slate);border-color:#111}
.silver .btn-buy{background:var(--forest);border-color:var(--mint)}
.gold .btn-buy{background:var(--amber);border-color:var(--amber-light)}

/* footer */
.site-footer{left:0;top:938px;width:1116px;height:202px;background:var(--leaf-dark);border-top:1px solid #6d8a2a}
.footer-col h4{font-family:"Oswald",sans-serif;font-weight:300;font-size:23px;color:var(--amber)}
.footer-links{list-style:none;margin-top:8px;font-family:"Oswald",sans-serif;font-weight:300;font-size:15px;color:var(--white)}
.footer-links li{height:25px;line-height:25px}
.field{left:415px;width:280px;height:29px;background:var(--white);font-size:12px;color:#888;line-height:29px;padding-left:8px}
.btn-subscribe{left:415px;top:1087px;width:98px;height:29px;line-height:25px;font-size:17px;background:var(--forest);border:2px solid var(--mint)}
.contact-lines{left:740px;top:984px;font-family:"Oswald",sans-serif;font-weight:300;font-size:15px;color:var(--white);line-height:25px}
.social{top:1074px;width:48px;height:48px;border-radius:50%;border:2px solid var(--white);background:var(--forest)}
.social.first{background:var(--amber)}
.social svg{position:absolute;left:12px;top:13px}
.copyright{left:0;top:1160px;width:1116px;text-align:center;font-size:12px;color:var(--white)}
.copyright b{text-decoration:underline}
</style>
</head>
<body>

<header>
  <svg class="abs brand-plate" viewBox="0 0 366 168" aria-hidden="true">
    <polygon points="0,0 366,0 366,130 183,168 0,130" fill="#3a4d10" transform="translate(0,4)"/>
    <polygon points="0,0 366,0 366,126 183,164 0,126" fill="#fff"/>
  </svg>
  <div class="abs brand-dot"></div>
  <div class="abs brand-name">VERDANT LODGE 17</div>
  <div class="abs account">Register<span>|</span>Login</div>
  <nav class="abs main-nav">
    <a class="current" href="#">HOME</a>
    <a href="#">ABOUT</a>
    <a href="#">SERVICES</a>
    <a href="#">TESTIMONIAL</a>
    <a href="#">CONTACT US</a>
  </nav>
</header>

<section>
  <div class="abs hero" role="img" aria-label="Background photo of cannabis leaves"></div>
  <div class="abs slider-frame"></div>
  <div class="abs slide-photo" role="img" aria-label="Photo of hands tending a young cannabis plant"></div>
  <svg class="abs slide-arrow" style="left:100px" viewBox="0 0 22 50" aria-hidden="true"><polyline points="20,2 2,25 20,48" fill="none" stroke="#fff" stroke-width="2"/></svg>
  <svg class="abs slide-arrow" style="left:686px" viewBox="0 0 22 50" aria-hidden="true"><polyline points="2,2 20,25 2,48" fill="none" stroke="#fff" stroke-width="2"/></svg>
  <div class="abs slide-caption">Supporting the care &amp; cultivation of cannabis</div>

  <div class="abs welcome-frame"></div>
  <div class="abs welcome-card">
    <h2>Welcome to<strong>VERDANT LODGE 17</strong></h2>
    <p>Lorem Ipsum is simply dummy text of the printing and typesetting industry. Lorem Ipsum has been the industry's standard dummy text ever since the 1500s, when an unknown printer took a galley of type and scrambled it to make a type specimen book. It has survived not only five centuries.</p>
    <p>Lorem Ipsum is simply dummy text of the printing and typesetting industry. Lorem Ipsum has been the industry's standard</p>
    <a class="btn btn-more" href="#">READ MORE</a>
  </div>
</section>

<section>
  <div class="abs service bronze" style="left:74px">
    <svg width="310" height="80" viewBox="0 0 310 80" aria-hidden="true"><polygon points="0,0 310,0 310,47 155,76 0,47" fill="#1d2524"/><polygon points="0,0 310,0 310,43 155,72 0,43" fill="#2f3b3a"/></svg>
    <h3>Bronze Service</h3>
    <p>Lorem Ipsum is simply dummy text of the printing and typesetting industry. Lorem Ipsum has been the industry's standard dummy text ever since the 1500s, when an unknown printer took a galley of type and scrambled it to make a type specimen book. It has survived not only five</p>
    <p>Lorem Ipsum is simply dummy text of the printing and typesetting industry. Lorem Ipsum has been the industry's standard</p>
    <a class="btn btn-buy" href="#"><svg width="20" height="17" viewBox="0 0 20 17"><path d="M0 1h4l3 10h10l2-7H6" fill="none" stroke="#fff" stroke-width="2"/><circle cx="8" cy="15" r="1.8" fill="#fff"/><circle cx="16" cy="15" r="1.8" fill="#fff"/></svg>BUY</a>
  </div>
  <div class="abs service silver" style="left:403px">
    <svg width="310" height="80" viewBox="0 0 310 80" aria-hidden="true"><polygon points="0,0 310,0 310,47 155,76 0,47" fill="#075a2a"/><polygon points="0,0 310,0 310,43 155,72 0,43" fill="#0b7a3a"/></svg>
    <h3>Silver Service</h3>
    <p>Lorem Ipsum is simply dummy text of the printing and typesetting industry. Lorem Ipsum has been the industry's standard dummy text ever since the 1500s, when an unknown printer took a galley of type and scrambled it to make a type specimen book. It has survived not only five</p>
    <p>Lorem Ipsum is simply dummy text of the printing and typesetting industry. Lorem Ipsum has been the industry's standard</p>
    <a class="btn btn-buy" href="#"><svg width="20" height="17" viewBox="0 0 20 17"><path d="M0 1h4l3 10h10l2-7H6" fill="none" stroke="#fff" stroke-width="2"/><circle cx="8" cy="15" r="1.8" fill="#fff"/><circle cx="16" cy="15" r="1.8" fill="#fff"/></svg>BUY</a>
  </div>
  <div class="abs service gold" style="left:732px">
    <svg width="310" height="80" viewBox="0 0 310 80" aria-hidden="true"><polygon points="0,0 310,0 310,47 155,76 0,47" fill="#a85517"/><polygon points="0,0 310,0 310,43 155,72 0,43" fill="#d97a2e"/></svg>
    <h3>Gold Service</h3>
    <p>Lorem Ipsum is simply dummy text of the printing and typesetting industry. Lorem Ipsum has been the industry's standard dummy text ever since the 1500s, when an unknown printer took a galley of type and scrambled it to make a type specimen book. It has survived not only five</p>
    <p>Lorem Ipsum is simply dummy text of the printing and typesetting industry. Lorem Ipsum has been the industry's standard</p>
    <a class="btn btn-buy" href="#"><svg width="20" height="17" viewBox="0 0 20 17"><path d="M0 1h4l3 10h10l2-7H6" fill="none" stroke="#fff" stroke-width="2"/><circle cx="8" cy="15" r="1.8" fill="#fff"/><circle cx="16" cy="15" r="1.8" fill="#fff"/></svg>BUY</a>
  </div>
</section>

<footer>
  <div class="abs site-footer"></div>
  <div class="abs footer-col" style="left:88px;top:948px">
    <h4>Useful Links</h4>
    <ul class="footer-links">
      <li>HOME</li><li>ABOUT</li><li>SERVICES</li><li>TESTIMONIAL</li><li>CONTACT US</li>
    </ul>
  </div>
  <div class="abs footer-col" style="left:417px;top:948px"><h4>Subscribe to our Newsletter</h4></div>
  <div class="abs field" style="top:990px">Enter your name</div>
  <div class="abs field" style="top:1038px">Enter your email</div>
  <a class="abs btn btn-subscribe" href="#">Subscribe</a>

  <div class="abs footer-col" style="left:746px;top:948px"><h4>Contact With Us</h4></div>
  <div class="abs contact-lines">Office name, Area, City, State, Country<br>123 456 7890<br>hello@verdantlodge17.example</div>
  <div class="abs social first" style="left:741px"></div>
  <div class="abs social" style="left:809px"></div>
  <div class="abs social" style="left:877px"></div>
  <div class="abs social" style="left:945px">
    <svg width="20" height="18" viewBox="0 0 20 18" aria-hidden="true"><rect x="0" y="2" width="20" height="14" rx="2" fill="#fff"/><polyline points="1,3 10,10 19,3" fill="none" stroke="#0b7a3a" stroke-width="1.6"/></svg>
  </div>

  <div class="abs copyright">© <b>VERDANT LODGE 17</b> - 2014. All Rights Reserved.</div>
</footer>

</body>
</html>
```